Book Cover: QUIET FERN!

I have a book coming with two different cover pictures for two different markets. I would like to supply the images and have a designer please add text and have the book ready for e and for print. I attach the press picture of Marwick Books for the spine for both. The vectored butterfly is for the UK and Europe. The image of the stamp is for India, the US, the Phillipines, and beyond. Both images are royalty free on Pixelvault if you can find them at the right size, or I can email. Given that I have invited so many designers, I am also open to your inspiration. It is the story of a young mystic meeting Tevandra Kulisharan after his death through meditation and so on. It is about being in his touch with his lineage, and shares many discussions and story between the two.
Title: Quiet Fern
Subtitle: A Memoir
Author: Maren Tolliver (UK edition with butterfly) Maren Tolliver, Ph.D. (US edition with stamp)
please leave space for blurb on the back and I will add the text once we have the designer and design.
Thank you.

```html
<!DOCTYPE html>
<html lang="en">
<head>
<meta charset="utf-8">
<title>Quiet Fern — a memoir</title>
<link rel="stylesheet" href="https://fonts.googleapis.com/css2?family=Arimo:wght@400;700&display=swap">
<style>
  :root {
    --cover-yellow: #f2d838;
    --title-navy: #1d3a6a;
    --author-cyan: #16a6d8;
    --wing-orange: #ef7a3c;
    --wing-amber: #f6ad3a;
    --wing-teal: #1ba5c9;
    --wing-navy: #1d3a6a;
    --wing-peach: #f4a77e;
  }
  * { margin: 0; padding: 0; box-sizing: border-box; }
  html, body {
    width: 750px;
    height: 1200px;
    overflow: hidden;
    background: var(--cover-yellow);
  }
  .cover {
    position: relative;
    width: 750px;
    height: 1200px;
    background: var(--cover-yellow);
    font-family: "Arimo", Arial, sans-serif;
    text-align: center;
  }
  .cover-art {
    position: absolute;
    left: 96px;
    top: 146px;
    width: 558px;
    height: 344px;
    border-radius: 40px;
    background:
      linear-gradient(135deg, var(--wing-orange) 0%, var(--wing-amber) 25%, var(--wing-peach) 45%, var(--wing-teal) 65%, var(--wing-navy) 100%);
    opacity: 0.9;
  }
  .title {
    position: absolute;
    left: 0;
    right: 0;
    top: 622px;
    font-weight: 700;
    font-size: 100px;
    line-height: 1;
    letter-spacing: 1px;
    color: var(--title-navy);
    word-spacing: 18px;
  }
  .subtitle {
    position: absolute;
    left: 0;
    right: 0;
    top: 712px;
    font-weight: 400;
    font-size: 46px;
    line-height: 1;
    color: var(--title-navy);
  }
  .author {
    position: absolute;
    left: 0;
    right: 0;
    top: 944px;
    font-weight: 400;
    font-size: 58px;
    line-height: 1;
    color: var(--author-cyan);
  }
</style>
</head>
<body>
  <main class="cover">
    <div class="cover-art" role="img" aria-label="Geometric faceted butterfly in orange, amber, peach, teal and navy"></div>
    <h1 class="title">QUIET FERN</h1>
    <p class="subtitle">a memoir</p>
    <p class="author">Maren Tolliver</p>
  </main>
</body>
</html>
```